Luxury Toilet Rental Business. Wavelet Hire.

Wavelet Hire (the logo is in the uploaded files)
We RENT and SELL Luxury Trailer toilets.
- Show location, number, pricing, pictures.
- We have two stall trailers for rent AND 3 stall trailers
- We sell them too
- We want our phone number shown
- We are a local company
- Slogan: Elevate your event with Wavelet Hire. The Luxurious Loo
- We want a pricing portion
- We want the sizes shown
- We want the different rates/ prices shown
- We do 1 day rentals
- We do 1 week rentals
- We want the service area. We serve Los Angeles County, Orange County, Riverside County, San Bernardino County, and Palm Desert.
- Our location is in Santa Ana California

Target Market(s)

Event planners, wedding planners, venue planners, concerts, events, gatherings.

Industry/Entity Type

Luxury Toilet Rentals

Number of Pages Required

1 page

Font styles to use
Serif
Sans Serif

Colors
EE7325
F08F49
F5BC92
FAE3D3
FDF4ED

Requirements
Must have
• Location, pricing, pictures, available areas. Our slogan.
Nice to have
• I like the idea of having tabs that show price, a tab that shows our contact information, pictures, event ideas, and where we service (the areas we'll go to)

```html
<!DOCTYPE html>
<html lang="en">
<head>
<meta charset="utf-8">
<title>Wavelet Hire – The Luxurious Loo</title>
<link href="https://fonts.googleapis.com/css2?family=Krona+One&family=Poppins:wght@300;400;500;600;700&display=swap" rel="stylesheet">
<style>
:root{
  --orange:#EE7325;
  --orange-soft:#F08F49;
  --peach:#F5BC92;
  --blush:#FAE3D3;
  --cream:#FDF4ED;
  --ink:#2b2b2b;
  --text:#555;
  --slate:#5b5b5b;
  --mist:#efefef;
  --white:#fff;
  --black:#000;
}
*{box-sizing:border-box;margin:0;padding:0}
html,body{width:1200px;height:4289px;overflow:hidden}
body{position:relative;background:var(--white);font-family:"Poppins",sans-serif;color:var(--text)}
.abs{position:absolute}
.display{font-family:"Krona One",sans-serif;text-transform:uppercase;letter-spacing:-0.5px}
.section-title{position:absolute;left:0;width:1200px;text-align:center;font-size:25px;color:var(--ink)}
.photo{position:absolute}
/* header */
.site-header{position:absolute;left:0;top:0;width:1200px;height:98px;background:var(--white)}
.brand{position:absolute;left:55px;top:33px;font-family:"Krona One",sans-serif;font-size:24px;color:var(--orange);white-space:nowrap}
.nav a{position:absolute;top:40px;font-size:14px;font-weight:500;color:var(--ink);text-decoration:none}
.call{position:absolute;left:937px;top:0;width:263px;height:98px;background:var(--orange);color:var(--white)}
.call svg{position:absolute;left:33px;top:31px}
.call p{position:absolute;left:83px;top:28px;font-size:17px;font-weight:600;line-height:22px}
/* hero */
.hero{position:absolute;left:0;top:98px;width:1200px;height:519px;background:linear-gradient(90deg,#6c6c6c 0%,#808080 40%,#7b7a78 70%,#6f6d6a 100%)}
.hero-play{position:absolute;left:319px;top:218px}
.hero-title{position:absolute;left:679px;top:216px;font-size:23px;line-height:30px;color:var(--white)}
/* about */
.about-frame{position:absolute;left:126px;top:704px;width:658px;height:356px;border:2px solid var(--orange);border-right:none}
.about-frame::after{content:"";position:absolute;right:0;top:0;width:2px;height:30px;background:var(--orange)}
.about-title{position:absolute;left:171px;top:770px;font-size:25px;color:var(--ink)}
.about-text{position:absolute;left:171px;top:834px;width:432px;font-size:14px;line-height:24px}
.about-accent{position:absolute;left:862px;top:948px;width:183px;height:165px;background:var(--orange)}
.about-mount{position:absolute;left:654px;top:734px;width:381px;height:369px;background:#f2f2f2}
/* rates */
.rates{position:absolute;left:0;top:1205px;width:1200px;height:542px;background:var(--cream)}
.rate-tag{position:absolute;width:192px;height:83px;background:var(--orange);color:var(--white);font-weight:700;font-size:18px;line-height:23px;padding:18px 0 0 26px}
/* gallery */
.gallery{position:absolute;left:0;top:1747px;width:1200px;height:619px;background:var(--slate)}
/* pricing */
.pricing-frame{position:absolute;left:363px;top:2430px;width:709px;height:466px;border:2px solid var(--orange)}
.pricing-title{position:absolute;left:592px;top:2491px;font-size:25px;color:var(--ink)}
.pricing-text{position:absolute;left:592px;top:2533px;width:410px;font-size:14px;line-height:21px}
.price-list{position:absolute;left:594px;top:2625px;width:330px;list-style:none;font-size:20px;font-weight:300;color:var(--text)}
.price-list li{display:flex;height:36.7px;align-items:center}
.price-list span:first-child{width:231px}
/* service areas */
.areas-text{position:absolute;left:250px;top:3050px;width:700px;text-align:center;font-size:14px;line-height:19px}
.area{position:absolute;top:3117px;width:186px;text-align:center}
.area .disc{width:186px;height:186px;border-radius:50%}
.area p{margin-top:16px;font-size:15px;font-weight:600;color:var(--text);line-height:20px}
/* contact */
.contact{position:absolute;left:0;top:3461px;width:1200px;height:529px;background:var(--mist)}
.contact-text{position:absolute;left:280px;top:3569px;width:640px;text-align:center;font-size:14px;line-height:20px}
.field{position:absolute;background:var(--white);font-size:14px;color:#666;padding:12px 10px}
.submit{position:absolute;left:521px;top:3862px;width:158px;height:52px;background:var(--orange);color:var(--white);font-size:14px;font-weight:700;display:flex;align-items:center;justify-content:center;border:none}
/* footer */
.site-footer{position:absolute;left:0;top:3990px;width:1200px;height:299px;background:var(--black);color:var(--white)}
.footer-brand{position:absolute;left:0;width:1200px;top:42px;text-align:center;font-family:"Krona One",sans-serif;font-size:34px;color:var(--white)}
.footer-item{position:absolute;top:155px;font-size:15px;font-weight:600;line-height:20px}
.footer-item svg{position:absolute;left:-30px;top:4px}
.footer-rule{position:absolute;left:92px;top:208px;width:1016px;height:1px;background:#444}
.copyright{position:absolute;left:0;width:1200px;top:236px;text-align:center;font-size:17px}
</style>
</head>
<body>

<header class="site-header">
  <div class="brand">Wavelet Hire</div>
  <nav class="nav">
    <a style="left:320px">PRICING</a>
    <a style="left:418px">CONTACT</a>
    <a style="left:524px">PICTURES</a>
    <a style="left:636px">EVENT IDEAS</a>
    <a style="left:767px">WHERE WE SERVICE</a>
  </nav>
  <div class="call">
    <svg width="36" height="36" viewBox="0 0 36 36"><circle cx="18" cy="18" r="18" fill="#fff"/><path d="M12.5 10.5c1-.6 2-.4 2.5.5l1.5 2.8c.4.8.2 1.6-.5 2.1l-1 .8c.8 2 2.3 3.6 4.3 4.4l.8-1c.5-.7 1.4-.9 2.1-.5l2.8 1.5c.9.5 1.1 1.5.5 2.5l-.9 1.4c-.6.9-1.7 1.3-2.8 1-5.6-1.6-9.8-5.8-11.2-11.3-.3-1.1.1-2.2 1-2.8z" fill="#EE7325"/></svg>
    <p>CALL US:<br>0555 0142 087</p>
  </div>
</header>

<section class="hero" role="img" aria-label="Photo of a grey two-stall luxury restroom trailer with steps, parked on a yard">
  <svg class="hero-play" width="84" height="84" viewBox="0 0 84 84"><circle cx="42" cy="42" r="40" fill="none" stroke="#fff" stroke-width="2.5"/><path d="M34 27 L58 42 L34 57 Z" fill="none" stroke="#fff" stroke-width="2.5" stroke-linejoin="round"/></svg>
  <h1 class="hero-title display">Elevate your event<br>with Wavelet Hire.<br>The luxurious loo</h1>
</section>

<section class="about">
  <div class="about-frame"></div>
  <h2 class="about-title display">About us</h2>
  <p class="about-text">Lorem ipsum dolor sit amet, consectetur adipiscing elit, sed do eiusmod tempor incididunt ut labore et dolore magna aliqua. Quis ipsum suspendisse ultrices gravida. Risus commodo viverra maecenas accumsan lacus vel facilisis. Lorem ipsum dolor sit amet, consect loremetur adipiscing elit, sed do eiusmod tempor incididunt ut labore et dolore magna aliqua.</p>
  <div class="about-accent"></div>
  <div class="about-mount"></div>
  <div class="photo" style="left:664px;top:744px;width:371px;height:359px;background:linear-gradient(180deg,#e6e7e9 0%,#f1f1f1 60%,#c9ae88 100%)" role="img" aria-label="Trailer restroom interior with vessel sink, mirror and toilet"></div>
</section>

<section class="rates">
  <h2 class="section-title display" style="top:48px">Our retals &amp; rates</h2>
  <div class="photo" style="left:133px;top:110px;width:450px;height:353px;background:linear-gradient(180deg,#b8b4ac 0%,#8f8c87 55%,#a5a39f 100%)" role="img" aria-label="Two-stall restroom trailer parked outside a building"></div>
  <div class="photo" style="left:612px;top:110px;width:450px;height:353px;background:linear-gradient(160deg,#e4e5e8 0%,#f3f3f3 55%,#d8c3a3 100%)" role="img" aria-label="White vanity with vessel sink inside a trailer"></div>
  <div class="rate-tag" style="left:128px;top:364px">1 DAY RENTALS<br>$ 29.00</div>
  <div class="rate-tag" style="left:608px;top:364px">1 WEEK RENTALS<br>$ 59.00</div>
</section>

<section class="gallery">
  <h2 class="section-title display" style="top:80px;color:#fff">Our gallery</h2>
  <div class="photo" style="left:126px;top:145px;width:297px;height:388px;background:linear-gradient(160deg,#dcdcde 0%,#f2f2f2 55%,#d6c09f 100%)" role="img" aria-label="Vessel sink and vanity close-up"></div>
  <div class="photo" style="left:451px;top:145px;width:296px;height:388px;background:linear-gradient(180deg,#e3e4e6 0%,#f0f0f0 60%,#c9ad86 100%)" role="img" aria-label="Restroom stall with sink, mirror and toilet"></div>
  <div class="photo" style="left:774px;top:145px;width:294px;height:388px;background:linear-gradient(180deg,#b9bab9 0%,#7d7e80 50%,#9c9a96 100%)" role="img" aria-label="Three-stall restroom trailer with blue steps"></div>
</section>

<section class="pricing">
  <div class="pricing-frame"></div>
  <div class="photo" style="left:103px;top:2463px;width:428px;height:393px;background:linear-gradient(180deg,#e2e3e5 0%,#f1f1f1 60%,#c8ad87 100%)" role="img" aria-label="Trailer restroom stall with sink and toilet"></div>
  <h2 class="pricing-title display">Our pricing</h2>
  <p class="pricing-text">Lorem ipsum dolor sit amet, consectetur adipiscing elit, sed do eiusmod tempor incidid unt ut labore et dolore magna aliquuis ipsum suspendisse.</p>
  <ul class="price-list">
    <li><span>Weiusmodtempor</span><span>- $19.00</span></li>
    <li><span>Weiusmodtempor</span><span>- $19.00</span></li>
    <li><span>Kemodtempor</span><span>- $19.00</span></li>
    <li><span>Weiusmodtempor</span><span>- $19.00</span></li>
    <li><span>Weiusmodtempor</span><span>- $19.00</span></li>
    <li><span>Aiusmodmpor</span><span>- $19.00</span></li>
  </ul>
</section>

<section class="areas">
  <h2 class="section-title display" style="top:3010px">Service areas</h2>
  <p class="areas-text">Lorem ipsum dolor sit amet, consectetur adipiscing elit, sed do eiusmod tempor incidid unt ut labore et dolore magna aliqua. Quis ipsum suspendisse ultrices gravida.</p>
  <div class="area" style="left:103px"><div class="disc" role="img" aria-label="Los Angeles skyline" style="background:linear-gradient(180deg,#5d8fc9,#6a5a4a)"></div><p>Los Angeles<br>County</p></div>
  <div class="area" style="left:306px"><div class="disc" role="img" aria-label="Orange County city view" style="background:linear-gradient(180deg,#4f9be0,#5aa08e)"></div><p>Orange<br>County</p></div>
  <div class="area" style="left:506px"><div class="disc" role="img" aria-label="Riverside bridge and river" style="background:linear-gradient(180deg,#8eb0d2,#7a6a5a)"></div><p>Riverside<br>County</p></div>
  <div class="area" style="left:707px"><div class="disc" role="img" aria-label="San Bernardino lakeside" style="background:linear-gradient(180deg,#4a8ed8,#2f6a8a)"></div><p>San Bernardino<br>County</p></div>
  <div class="area" style="left:910px"><div class="disc" role="img" aria-label="Palm Desert palms and mountains" style="background:linear-gradient(180deg,#6f9ad0,#b89f7a)"></div><p>Palm Desert</p></div>
</section>

<section class="contact">
  <h2 class="section-title display" style="top:72px">Contact us</h2>
</section>
<p class="contact-text">Lorem ipsum dolor sit amet, consectetur adipiscing elit, sed do eiusmod tempor incidid unt ut labore et dolore magna aliquuis ipsum suspendisse.</p>
<form>
  <div class="field" style="left:270px;top:3646px;width:324px;height:46px">Name:</div>
  <div class="field" style="left:606px;top:3646px;width:323px;height:46px">Email:</div>
  <div class="field" style="left:270px;top:3702px;width:324px;height:47px">Phone:</div>
  <div class="field" style="left:606px;top:3702px;width:323px;height:47px">Subject:</div>
  <div class="field" style="left:270px;top:3759px;width:659px;height:130px">Message:</div>
  <button class="submit" type="button">SUBMIT NOW</button>
</form>

<footer class="site-footer">
  <div class="footer-brand">Wavelet Hire</div>
  <div class="footer-item" style="left:225px">
    <svg width="24" height="18" viewBox="0 0 24 18"><rect x="1" y="1" width="22" height="16" rx="2" fill="#EE7325"/><path d="M2 2l10 8 10-8" fill="none" stroke="#000" stroke-width="1.6"/></svg>
    Email:<br>info@WaveletHire.com
  </div>
  <div class="footer-item" style="left:592px">
    <svg width="24" height="26" viewBox="0 0 24 24"><path d="M5 2.5c1-.6 2-.4 2.5.5l2 3.5c.4.8.2 1.7-.5 2.2l-1.3 1c1 2.5 3 4.6 5.6 5.6l1-1.3c.5-.7 1.4-.9 2.2-.5l3.5 2c.9.5 1.1 1.5.5 2.5l-1.1 1.7c-.7 1.1-2 1.6-3.3 1.2-6.6-2-11.6-7-13.5-13.5-.4-1.3.1-2.6 1.2-3.3z" fill="#EE7325"/></svg>
    Phone:<br>555 xx x0193
  </div>
  <div class="footer-item" style="left:800px">
    <svg width="20" height="26" viewBox="0 0 20 26"><path d="M10 1C5 1 1.5 4.8 1.5 9.5 1.5 16 10 25 10 25s8.5-9 8.5-15.5C18.5 4.8 15 1 10 1z" fill="#EE7325"/><circle cx="10" cy="9.5" r="3.3" fill="#000"/></svg>
    Address:<br>Lorem dumy text 098
  </div>
  <div class="footer-rule"></div>
  <p class="copyright">©2024 Wavelet Hire. All rights are reserved.</p>
</footer>

</body>
</html>
```